Business cards, e-mail signature, letterhead
Noral Studio, Inc
Business cards, e-mail signature, letterhead - Communications and Media
Creative Brief
Bright & Fun-filled
Tobin Varley
President, Noral Studio Inc.
Card: New York City Letterhead: 47 West 112th St. 9F New York, NY 10031
skype: tobinvarley604
tbnvrl@quillpost.net
www.NoralStudio.com
Locations of our properties can be listed on the back of card (see below) and incorporated into letterhead.
Ash Fork, AZ / Ashtabula, OH/ Belle Rose, LA/ Blanca, CO/ Cross City, FL/ Dulac, LA/ Huntington, OR/ Islamorada, FL/ Lead, SD/ Mona, UT/ Morgan, GA/ Ty Ty, GA/ Winchester, VA

```html
<!DOCTYPE html>
<html lang="en">
<head>
<meta charset="utf-8">
<title>Noral Studio Inc. — Business Card</title>
<link rel="stylesheet" href="https://fonts.googleapis.com/css2?family=Montserrat:wght@600;700&family=Open+Sans:wght@400;600&display=swap">
<style>
  :root {
    --backdrop: #e4e5e8;
    --blue-deep: #1b2f8f;
    --blue-mid: #2c4fc0;
    --blue-bright: #3f6fe0;
    --paper: #ffffff;
    --ink: #2a2f45;
    --ink-soft: #5a607a;
    --rule: #c9cde0;
  }
  * { box-sizing: border-box; margin: 0; padding: 0; }
  html, body { width: 1200px; height: 1009px; overflow: hidden; }
  body {
    background: var(--backdrop);
    position: relative;
    font-family: "Open Sans", Arial, sans-serif;
    color: var(--ink);
  }
  .card {
    position: absolute;
    width: 600px;
    height: 343px;
    border-radius: 18px;
    overflow: hidden;
    box-shadow: 0 10px 26px rgba(20, 30, 70, 0.22);
  }

  /* Back of card */
  .card-back {
    left: 540px;
    top: 150px;
    background: radial-gradient(circle at 70% 65%, var(--blue-bright) 0%, var(--blue-mid) 40%, var(--blue-deep) 100%);
    color: var(--paper);
    padding: 28px 40px;
  }
  .card-back .company-name {
    font-family: "Montserrat", Arial, sans-serif;
    font-weight: 700;
    font-size: 27px;
    letter-spacing: 1px;
    margin-bottom: 16px;
  }
  .locations { list-style: none; }
  .locations li {
    font-size: 12.5px;
    line-height: 19px;
    padding-left: 14px;
    position: relative;
  }
  .locations li::before {
    content: "";
    position: absolute;
    left: 0; top: 8px;
    width: 5px; height: 5px;
    border-radius: 50%;
    background: var(--paper);
  }

  /* Front of card */
  .card-front {
    left: 70px;
    top: 560px;
    background: var(--paper);
  }
  .band {
    position: absolute;
    left: 0; right: 0;
    height: 44px;
    background: linear-gradient(90deg, var(--blue-deep), var(--blue-mid) 60%, var(--blue-bright));
  }
  .band-top { top: 0; }
  .band-bottom { bottom: 0; }
  .band::after {
    content: "";
    position: absolute;
    left: 0; right: 0;
    height: 4px;
    background: var(--rule);
  }
  .band-top::after { bottom: -8px; }
  .band-bottom::after { top: -8px; }

  .brand {
    position: absolute;
    left: 34px;
    top: 108px;
    width: 240px;
    display: flex;
    flex-direction: column;
    align-items: center;
  }
  .brand-dot {
    width: 70px; height: 70px;
    border-radius: 50%;
    background: var(--blue-mid);
    margin-bottom: 12px;
  }
  .brand-name {
    font-family: "Montserrat", Arial, sans-serif;
    font-weight: 700;
    font-size: 25px;
    color: var(--blue-deep);
    white-space: nowrap;
  }
  .divider {
    position: absolute;
    left: 300px;
    top: 78px;
    bottom: 78px;
    width: 1px;
    background: var(--rule);
  }
  .contact {
    position: absolute;
    left: 322px;
    top: 84px;
    font-size: 13px;
    color: var(--ink-soft);
  }
  .contact .person {
    font-family: "Montserrat", Arial, sans-serif;
    font-weight: 600;
    font-size: 17px;
    color: var(--blue-deep);
  }
  .contact .role { margin-bottom: 18px; }
  .contact .city { margin-bottom: 6px; color: var(--ink); }
  .contact-line {
    display: flex;
    align-items: center;
    gap: 7px;
    line-height: 20px;
  }
  .contact-line svg { width: 12px; height: 12px; fill: var(--blue-mid); flex: none; }
</style>
</head>
<body>

<section class="card card-back" aria-label="Card back">
  <p class="company-name">NORAL STUDIO INC.</p>
  <ul class="locations">
    <li>Ash Fork, AZ</li>
    <li>Ashtabula, OH</li>
    <li>Belle Rose, LA</li>
    <li>Blanca, CO</li>
    <li>Cross City, FL</li>
    <li>Dulac, LA</li>
    <li>Huntington, OR</li>
    <li>Islamorada, FL</li>
    <li>Lead, SD</li>
    <li>Mona, UT</li>
    <li>Morgan, GA</li>
    <li>Ty Ty, GA</li>
  </ul>
</section>

<section class="card card-front" aria-label="Card front">
  <div class="band band-top"></div>
  <div class="brand">
    <span class="brand-dot"></span>
    <span class="brand-name">NORAL STUDIO INC.</span>
  </div>
  <div class="divider"></div>
  <div class="contact">
    <p class="person">Tobin Varley</p>
    <p class="role">President, Noral Studio Inc.</p>
    <p class="city">New York City</p>
    <p class="contact-line">
      <svg viewBox="0 0 24 24" aria-hidden="true"><path d="M6.6 10.8a15.1 15.1 0 0 0 6.6 6.6l2.2-2.2c.3-.3.7-.4 1-.2 1.1.4 2.3.6 3.6.6.6 0 1 .4 1 1V20c0 .6-.4 1-1 1C10.6 21 3 13.4 3 4c0-.6.4-1 1-1h3.5c.6 0 1 .4 1 1 0 1.3.2 2.5.6 3.6.1.3 0 .7-.2 1z"/></svg>
      (917) 555-0148
    </p>
    <p class="contact-line">
      <svg viewBox="0 0 24 24" aria-hidden="true"><circle cx="12" cy="12" r="10"/></svg>
      tobinvarley604
    </p>
    <p class="contact-line">
      <svg viewBox="0 0 24 24" aria-hidden="true"><path d="M2 5h20v14H2z M3.5 6.5 12 13l8.5-6.5" /></svg>
      tbnvrl@quillpost.net
    </p>
  </div>
  <div class="band band-bottom"></div>
</section>

</body>
</html>
```